Business Card - connecting 2 souls and beggining the journey of self discovery

Logo on the front
with tag line

On the back list of services and contact details

Seminars
workshops
Coaching
podcasts

Darren Whitlow
Health & Wellbeing Life Coach
0468 215 937
darren@wearebrightroots.net
wearebrightroots.net

Industry/Entity Type

Life Coaching

Contact Information for Business Card

I like the use of colour from the logo to be used. I'm not a fan of white.

Requirements
Must have
• My tagline: The journey home starts with you
Nice to have
• Use of colour that is in the mind body soul logo

```html
<!DOCTYPE html>
<html lang="en">
<head>
<meta charset="utf-8">
<title>Bright Roots Wellness – Business Card</title>
<link rel="stylesheet" href="https://fonts.googleapis.com/css2?family=Roboto:wght@400;500&display=swap">
<style>
  :root {
    --canvas: #e7e4df;
    --card: #323232;
    --ink: #f2f2f2;
    --name-green: #9ccb3b;
    --icon-orange: #e98a3a;
    --band-green: #9ccb3b;
    --band-yellow: #d6c82a;
    --band-orange: #e9a95a;
    --band-pink: #d98a8a;
    --band-purple: #9b59a7;
    --mark: #e9a95a;
  }
  * { box-sizing: border-box; margin: 0; padding: 0; }
  html, body { width: 1200px; height: 1200px; overflow: hidden; }
  body {
    background: var(--canvas);
    font-family: "Roboto", Arial, sans-serif;
    color: var(--ink);
    position: relative;
  }
  .card {
    position: absolute;
    left: 213px;
    width: 773px;
    height: 437px;
    background: var(--card);
    box-shadow: 0 6px 18px rgba(0,0,0,0.25);
    overflow: hidden;
  }
  .card--front { top: 150px; }
  .card--back { top: 633px; }

  .band {
    position: absolute;
    left: 0; right: 0;
    top: 388px;
    height: 33px;
    background: linear-gradient(90deg, var(--band-green) 0%, var(--band-yellow) 40%, var(--band-orange) 58%, var(--band-pink) 78%, var(--band-purple) 100%);
    display: flex;
    align-items: center;
    font-size: 20px;
    color: #fffbe8;
  }
  .band--services { padding-left: 49px; gap: 10px; }
  .band--services .dot {
    width: 8px; height: 8px; border-radius: 50%; background: #fffbe8; display: inline-block;
  }
  .band--tagline { justify-content: center; font-size: 22px; }

  .identity { position: absolute; left: 49px; top: 76px; }
  .identity__name { font-size: 32px; font-weight: 500; color: var(--name-green); line-height: 1; }
  .identity__role { font-size: 20px; margin-top: 10px; }

  .address { position: absolute; left: 49px; top: 190px; font-size: 19px; line-height: 27px; }

  .contacts { position: absolute; left: 49px; top: 260px; list-style: none; font-size: 19px; }
  .contacts li { display: flex; align-items: center; gap: 8px; height: 27.5px; }
  .contacts svg { width: 18px; height: 18px; flex: none; }

  .brand { position: absolute; display: flex; flex-direction: column; align-items: center; }
  .brand__mark { border-radius: 50%; background: var(--mark); }
  .brand__name { font-weight: 400; color: var(--ink); white-space: nowrap; }
  .brand--front { left: 587px; top: 32px; transform: translateX(-50%); }
  .brand--front .brand__mark { width: 100px; height: 100px; }
  .brand--front .brand__name { font-size: 25px; margin-top: 20px; }
  .brand--back { left: 386px; top: 101px; transform: translateX(-50%); }
  .brand--back .brand__mark { width: 128px; height: 128px; }
  .brand--back .brand__name { font-size: 33px; margin-top: 28px; }
</style>
</head>
<body>
  <section class="card card--front" aria-label="Business card front">
    <div class="identity">
      <h1 class="identity__name">Darren Whitlow</h1>
      <p class="identity__role">Health &amp; Wellbeing Life Coach</p>
    </div>
    <address class="address" style="font-style:normal">
      742 Marlow Avenue, Suite 310<br>Fairview, CA 3061
    </address>
    <ul class="contacts">
      <li>
        <svg viewBox="0 0 24 24" fill="none" stroke="var(--icon-orange)" stroke-width="1.8"><path d="M5 3h4l2 5-2.5 1.5a11 11 0 0 0 6 6L16 13l5 2v4a2 2 0 0 1-2 2A17 17 0 0 1 3 5a2 2 0 0 1 2-2z"/></svg>
        0468 215 937
      </li>
      <li>
        <svg viewBox="0 0 24 24" fill="none" stroke="var(--icon-orange)" stroke-width="1.8"><rect x="6.5" y="2" width="11" height="20" rx="2"/><line x1="10.5" y1="18.5" x2="13.5" y2="18.5"/></svg>
        000-000-0000
      </li>
      <li>
        <svg viewBox="0 0 24 24" fill="none" stroke="var(--icon-orange)" stroke-width="1.8"><rect x="2.5" y="5" width="19" height="14"/><path d="M2.5 5l9.5 8 9.5-8"/></svg>
        darren@wearebrightroots.net
      </li>
      <li>
        <svg viewBox="0 0 24 24" fill="none" stroke="var(--icon-orange)" stroke-width="1.8"><circle cx="12" cy="12" r="9.5"/><ellipse cx="12" cy="12" rx="4" ry="9.5"/><line x1="2.5" y1="12" x2="21.5" y2="12"/></svg>
        www.wearebrightroots.net
      </li>
    </ul>
    <div class="brand brand--front">
      <div class="brand__mark"></div>
      <p class="brand__name">Bright Roots Wellness</p>
    </div>
    <div class="band band--services">
      <span>Seminars</span><span class="dot"></span>
      <span>workshops</span><span class="dot"></span>
      <span>Coaching</span><span class="dot"></span>
      <span>podcasts</span>
    </div>
  </section>

  <section class="card card--back" aria-label="Business card back">
    <div class="brand brand--back">
      <div class="brand__mark"></div>
      <p class="brand__name">Bright Roots Wellness</p>
    </div>
    <div class="band band--tagline">The journey home starts with you</div>
  </section>
</body>
</html>
```